Business Card Design

I would like a double sided business card design.

1 side showing usual contact details and small version of logo (attached "GlanMare")

other side with larger logo and artwork with room to list what we specialise in.

Glan Mare is a Fashion Millinery Design and Sales Business.

I have attached some other examples of te styles i like so you can see what sort of taste i have.

Feel free to play around with colours of logo - it is grey as i originall had in mind a black background with monochrome silver logo.
Updates

• Please send me a message with your quote after posting your design. Budget set at Minimum (FYI) and negotiable
• Supporting files are examples only - i do not wish to copy them.  The only file for exact use is my logo "GlanMare"
• Thank you

Target Market(s)

18 - 80 yo females mainly

Industry/Entity Type

Business

Requirements
Must have
• unique and striking individuality
Should not have
• boring and normal

```html
<!DOCTYPE html>
<html lang="en">
<head>
<meta charset="utf-8">
<title>GlanMare Business Card – Front and Back</title>
<link rel="stylesheet" href="https://fonts.googleapis.com/css2?family=Pinyon+Script&family=Poiret+One&display=swap">
<style>
  :root {
    --canvas: #ffffff;
    --card-light: #ffffff;
    --card-dark: #2a2829;
    --band-dark: #1f1e1f;
    --logo-panel: #0b0b0c;
    --panel-edge: #4a4a4c;
    --ink: #111111;
    --ink-soft: #6e6e6e;
    --silver: #d9d9d9;
    --silver-deep: #8c8c8c;
    --ornament: #9a9a9a;
    --trim: #9c9c9c;
  }
  * { margin: 0; padding: 0; box-sizing: border-box; }
  html, body {
    width: 1200px; height: 1200px; overflow: hidden;
    background: var(--canvas);
  }
  .canvas { position: relative; width: 1200px; height: 1200px; }

  .card {
    position: absolute; left: 179px; width: 849px; height: 487px; overflow: hidden;
  }
  .card--front { top: 86px; background: var(--card-light); border: 1px solid var(--trim); }
  .card--back { top: 650px; background: var(--card-dark); }

  .ornament { position: absolute; }
  .ornament--top-left {
    left: 0; top: 0; width: 446px; height: 120px;
    background: radial-gradient(ellipse at 40% 20%, rgba(150,150,150,.35), rgba(150,150,150,0) 70%);
  }
  .ornament--top-right {
    right: 0; top: 0; width: 384px; height: 145px;
    background: radial-gradient(ellipse at 75% 35%, rgba(60,60,60,.32), rgba(60,60,60,0) 70%);
  }
  .ornament--bottom-left {
    left: 0; bottom: 0; width: 571px; height: 183px;
    background: radial-gradient(ellipse at 35% 75%, rgba(70,70,70,.4), rgba(70,70,70,0) 70%);
  }

  .logo-panel {
    position: absolute; background: var(--logo-panel);
    display: flex; align-items: center; justify-content: center;
  }
  .card--front .logo-panel {
    left: 29px; top: 158px; width: 281px; height: 117px; border-radius: 12px;
  }
  .brand-name {
    font-family: "Poiret One", sans-serif; font-weight: 400;
    color: var(--silver); letter-spacing: 0.5px;
  }
  .card--front .brand-name { font-size: 44px; }

  .holder-name {
    position: absolute; right: 20px; top: 162px;
    font-family: "Pinyon Script", cursive; font-size: 32px; color: var(--ink);
  }
  .divider {
    position: absolute; left: 321px; top: 211px; width: 526px; height: 5px;
    background: linear-gradient(to bottom, #3a3a3a, #e6e6e6 50%, #3a3a3a);
  }
  .job-position {
    position: absolute; right: 22px; top: 222px;
    font-family: "Pinyon Script", cursive; font-size: 26px; color: var(--ink-soft);
  }
  .contact {
    position: absolute; right: 22px; top: 374px; text-align: right;
    font-family: "Pinyon Script", cursive; font-size: 19px; line-height: 28px; color: var(--ink);
  }
  .contact .gap { display: inline-block; width: 18px; }

  .pattern {
    position: absolute; inset: 0;
    background:
      radial-gradient(circle at 15% 25%, rgba(120,120,120,.18), rgba(120,120,120,0) 35%),
      radial-gradient(circle at 85% 40%, rgba(120,120,120,.16), rgba(120,120,120,0) 35%),
      radial-gradient(circle at 50% 90%, rgba(120,120,120,.12), rgba(120,120,120,0) 40%);
  }
  .glow {
    position: absolute; left: 240px; top: 270px; width: 370px; height: 80px;
    background: radial-gradient(ellipse at 50% 20%, rgba(190,190,190,.55), rgba(190,190,190,0) 70%);
  }
  .card--back .logo-panel {
    left: 184px; top: 80px; width: 487px; height: 203px; border-radius: 24px;
    border: 1px solid var(--panel-edge);
  }
  .card--back .brand-name { font-size: 84px; }
  .services-band {
    position: absolute; left: 0; top: 332px; width: 100%; height: 88px;
    background: var(--band-dark);
    display: flex; align-items: center; justify-content: center;
  }
  .services-text {
    font-family: "Pinyon Script", cursive; font-size: 25px; color: #f2f2f2; letter-spacing: 0.5px;
  }
</style>
</head>
<body>
<main class="canvas">
  <section class="card card--front" aria-label="Card front">
    <div class="ornament ornament--top-left" role="img" aria-label="Silver flourish swirls along the top left edge"></div>
    <div class="ornament ornament--top-right" role="img" aria-label="Dark grey flourish swirls in the top right corner"></div>
    <div class="ornament ornament--bottom-left" role="img" aria-label="Grey leaf and scroll flourishes along the bottom left edge"></div>

    <div class="logo-panel"><span class="brand-name">GlanMare</span></div>

    <p class="holder-name">Card Holder Name</p>
    <div class="divider"></div>
    <p class="job-position">Job Position</p>

    <address class="contact" style="font-style:normal">
      Phone: 111 - 222 - 3333<span class="gap"></span>Fax: 111 - 222 - 3333<br>
      E-mail: yourname@email.com<br>
      Website: www.website.com
    </address>
  </section>

  <section class="card card--back" aria-label="Card back">
    <div class="pattern" role="img" aria-label="Faint silver line flourish pattern across the dark background"></div>
    <div class="glow"></div>
    <div class="logo-panel"><span class="brand-name">GlanMare</span></div>
    <div class="services-band">
      <p class="services-text">List of specializations, ads, services and more</p>
    </div>
  </section>
</main>
</body>
</html>
```